Holiday Card for Consulting Business

Lumisk Studio helps large and mid-sized companies communicate with their employees, specifically using digital media and events.

We need a holiday card for our clients.

GRAPHICS
Do not use any religious symbols.
Ideas of graphic elements we like are: snowflakes, stars, NYC skyline or other city scenes, foil wrapping paper, bows, penguins, white puppies or reindeer.

We have a very modern aesthetic.

COLORS
Use our brand color -- purple and orange and to represent the holidays, use Silver, White and/or Black.

Target Market(s)

Human resource, information technology professionals, executives and vendors

Industry/Entity Type

Religious

Font styles to use
Sans Serif
Script

Colors
6b449b
faa54b
000000
e9e9e9
c4c4c4
ffffff

Requirements
Must have
• CMYK, 300 DPI format since I plan to print it.
My logo -- Use the Lumisk Studio version, NOT Lumisk Teal Studio

CONTENT
Outside Front: Seasons Greetings

Inside: Enthusiastic and warm wishes for a peaceful, joyous holiday and fantastic New Year!

Outside Back (i've attached an example):
Workforce Messaging Devotees sign
Y logo with Corporate and employee communication | Creative multimedia communication campaigns | Change management | Employee engagement | Internal branding | Web architecture and content | Strategic and tactical planning
Nice to have
• Ideas of graphic elements we like are: snowflakes, stars, NYC skyline or other city scenes, foil wrapping paper, bows, penguins, white puppies or reindeer.

Horizontal orientation.
Should not have
• Religious symbols.

```html
<!DOCTYPE html>
<html lang="en">
<head>
<meta charset="utf-8">
<title>Lumisk Studio Holiday Card</title>
<link rel="stylesheet" href="https://fonts.googleapis.com/css2?family=Montserrat:wght@300;400;600;800&family=Great+Vibes&display=swap">
<style>
  :root {
    --brand-purple: #6b449b;
    --brand-purple-light: #9a5cc4;
    --brand-purple-deep: #4e2a7f;
    --brand-orange: #faa54b;
    --silver: #c4c4c4;
    --silver-light: #e9e9e9;
    --ink: #000000;
    --paper: #ffffff;
    --text-grey: #4a4a4a;
  }
  html, body {
    margin: 0;
    padding: 0;
    width: 1200px;
    height: 256px;
    overflow: hidden;
    background: var(--paper);
  }
  .card-spread {
    position: relative;
    width: 1200px;
    height: 256px;
    font-family: "Montserrat", Arial, sans-serif;
  }

  /* Outside front */
  .front-cover {
    position: absolute;
    left: 0;
    top: 0;
    width: 390px;
    height: 252px;
    overflow: hidden;
    background:
      radial-gradient(ellipse at 60% 8%, rgba(255,190,240,0.55), transparent 55%),
      linear-gradient(180deg, var(--brand-purple-light) 0%, var(--brand-purple) 55%, var(--brand-purple-deep) 100%);
  }
  .reindeer-art {
    position: absolute;
    left: 268px;
    top: 44px;
    width: 118px;
    height: 92px;
    border-radius: 40%;
    background: radial-gradient(ellipse, rgba(255,255,255,0.35), rgba(255,255,255,0) 70%);
  }
  .flourish-art {
    position: absolute;
    left: 18px;
    top: 76px;
    width: 84px;
    height: 90px;
    border-radius: 40%;
    background: radial-gradient(ellipse, rgba(255,255,255,0.3), rgba(255,255,255,0) 70%);
  }
  .skyline-art {
    position: absolute;
    left: 0;
    bottom: 0;
    width: 390px;
    height: 78px;
    background: linear-gradient(180deg, rgba(190,140,220,0.45), rgba(170,120,205,0.8));
  }
  .snowflake-band {
    position: absolute;
    left: 0;
    bottom: 0;
    width: 390px;
    height: 30px;
    background: linear-gradient(180deg, rgba(255,255,255,0.2), rgba(255,255,255,0.75));
  }
  .greeting-script {
    position: absolute;
    left: 100px;
    top: 86px;
    margin: 0;
    font-family: "Great Vibes", cursive;
    font-weight: 400;
    font-size: 48px;
    line-height: 1;
    color: var(--silver-light);
  }
  .greeting-block {
    position: absolute;
    left: 86px;
    top: 130px;
    margin: 0;
    font-family: "Montserrat", Arial, sans-serif;
    font-weight: 800;
    font-size: 33px;
    letter-spacing: 1px;
    line-height: 1;
    color: var(--brand-orange);
  }

  /* Inside message */
  .inside-message {
    position: absolute;
    left: 433px;
    top: 104px;
    width: 320px;
    text-align: center;
    color: var(--text-grey);
    white-space: nowrap;
  }
  .message-line {
    margin: 0;
    font-weight: 400;
    font-size: 9.5px;
    letter-spacing: 2.6px;
    line-height: 15px;
    text-transform: uppercase;
  }
  .message-accent {
    color: var(--silver);
    font-weight: 800;
  }
  .message-script {
    margin: 3px 0 0;
    font-family: "Great Vibes", cursive;
    font-size: 24px;
    line-height: 1;
    color: var(--ink);
  }

  /* Outside back: signature */
  .brand-sign {
    position: absolute;
    left: 858px;
    top: 56px;
    width: 270px;
    text-align: center;
  }
  .brand-name {
    margin: 0;
    font-family: "Montserrat", Arial, sans-serif;
    font-weight: 800;
    font-size: 38px;
    line-height: 44px;
    color: var(--brand-purple);
  }
  .brand-tagline {
    margin: 10px 0 0;
    font-weight: 600;
    font-size: 8px;
    color: var(--brand-orange);
  }
  .service-list {
    margin: 8px 0 0;
    font-weight: 400;
    font-size: 6px;
    line-height: 9px;
    color: var(--text-grey);
  }
</style>
</head>
<body>
  <main class="card-spread">
    <section class="front-cover">
      <div class="skyline-art" role="img" aria-label="City skyline silhouette in soft lavender"></div>
      <div class="snowflake-band" role="img" aria-label="Row of white snowflakes along the bottom edge"></div>
      <div class="flourish-art" role="img" aria-label="Decorative swirling white flourish"></div>
      <div class="reindeer-art" role="img" aria-label="Leaping reindeer made of silver stars and snowflakes"></div>
      <h1 class="greeting-script">Season's</h1>
      <p class="greeting-block">GREETINGS</p>
    </section>

    <section class="inside-message">
      <p class="message-line">Enthusiastic and warm <span class="message-accent">wishes</span> for</p>
      <p class="message-line">a <span class="message-accent">peaceful</span>, joyous holiday</p>
      <p class="message-line">and a <span class="message-accent">fantastic</span></p>
      <p class="message-script">New Year!</p>
    </section>

    <section class="brand-sign">
      <p class="brand-name">Lumisk<br>Studio</p>
      <p class="brand-tagline">Workforce Messaging Devotees</p>
      <p class="service-list">Corporate and employee communication | Creative multimedia communication campaigns | Change management | Employee engagement | Internal branding | Web architecture and content | Strategic and tactical planning</p>
    </section>
  </main>
</body>
</html>
```